Sweet website for Wrenfield Flowers

Our name is Wrenfield and we are looking for someone to design a SWEET looking website for us. We would like a site that has a responsive design, clean interface, easy to navigate and smooth user experience. It will be hosted on wordpress and is an ecommerce site so it needs to be fully compatible so that updates can be made easily on the back end.

It is important to us that the design is premium looking, beautiful to look at and has an elegance to it that befits the beautiful products we sell. We don't want it to look like a standard wordpress template so please feel free to be creative.

We have defined basic template pages in wireframes which are NOT by any means a design mandate. Please use this as a guide for what content should be considered in the design on each page. THERE ARE TWO HOMEPAGE OPTIONS (1 has additional content areas - please propose designs for both options) We DO NOT want to see creative that looks exactly like our wireframes. Please come up with fresh creative ideas. (see wireframe doc attached). We have also attached the copy deck, logos, design references to help you to better understand what our customers like.

THANK YOU! LOOKING FORWARD TO SEEING YOUR PROPOSALS!!!
Updates

An updated content/wireframe document has been uploaded. We have 2 content options for the homepage - please propose designs for both layouts.

We have also added a powerpoint with websites that we like so that you can get a better idea of what we would like our website to look like.

Project Deadline Extended
Reason: We are extending the deadline and have increased and guaranteed the payment since we can see potential in the submitted designs but feel that they are currently not at their creative potential. The extra time given should allow for more time to submit original designs that do not look exactly like the wireframes provided.

Target Market(s)

Premium, affluent market

Font styles to use
Sans Serif

Requirements
Must have
• see wireframe, copy and design reference attachments and use as guidelines. The powerpoint presentation shows key areas that we think will be good in our design. Please review them. There are 2 homepage content options. Please propose options for both.
Please take note that option 2 has 3 additional content areas labelled "hand tied bouquets shop now", "Hatbox arrangements shop now" "floral cupcakes shop now" please propose 1 design with this the additional sections and 1 design without.

```html
<!DOCTYPE html>
<html lang="en">
<head>
<meta charset="utf-8">
<title>Wrenfield Flowers</title>
<link rel="stylesheet" href="https://fonts.googleapis.com/css2?family=Arimo:wght@400;700&display=swap">
<style>
:root{
  --plum:#5d2445;
  --plum-dark:#4a1a36;
  --pink:#d9587f;
  --pink-light:#ec8fae;
  --pink-soft:#fde9f1;
  --rose-title:#c9436e;
  --ink:#3a3a3a;
  --white:#ffffff;
  --footer:#2f2f2f;
  --button:#1f1f1f;
  --flourish:rgba(190,80,130,.35);
}
*{box-sizing:border-box;margin:0;padding:0}
html,body{width:1200px;height:899px;overflow:hidden}
body{
  position:relative;
  background:radial-gradient(ellipse at 50% 30%,#6a2a4f 0%,var(--plum) 55%,var(--plum-dark) 100%);
  font-family:"Arimo",Arial,sans-serif;color:var(--ink);
}
a{text-decoration:none;color:inherit}
.flourish{position:absolute;border-radius:50%;pointer-events:none;
  background:radial-gradient(ellipse at center,var(--flourish) 0%,rgba(190,80,130,.12) 55%,rgba(190,80,130,0) 75%)}
.flourish-left{left:55px;top:260px;width:150px;height:210px}
.flourish-top{left:790px;top:-40px;width:420px;height:150px}
.flourish-right{left:1035px;top:480px;width:100px;height:110px}
.brand{position:absolute;left:157px;top:54px;display:flex;align-items:center;gap:8px;
  color:var(--pink-light);font-size:19px;letter-spacing:2px;text-transform:uppercase}
.brand-dot{width:12px;height:12px;border-radius:50%;background:var(--pink-light)}
.search-tab{position:absolute;left:430px;top:48px;width:340px;height:50px;
  background:linear-gradient(#7a3560,#6b2b52);border-radius:30px 30px 0 0}
.search{position:absolute;left:493px;top:59px;width:214px;height:28px;border-radius:3px;
  background:linear-gradient(#d8b8c8,#c9a4b7);border:1px solid #a77a92;display:flex;align-items:center}
.search span{flex:1;padding-left:5px;font-size:12px;color:#7b5769}
.search svg{margin:0 8px 0 6px}
.search i{width:1px;height:18px;background:#8d6378}
.account-links{position:absolute;top:26px;left:855px;display:flex;gap:20px;font-size:11px}
.account-links a{display:flex;align-items:center;gap:6px;color:var(--pink-light);text-decoration:underline}
.icon-round{width:24px;height:24px;border-radius:50%;background:#2e0e20;display:flex;align-items:center;justify-content:center}
.main-nav{position:absolute;left:156px;top:96px;width:890px;height:36px;border-radius:3px;
  background:linear-gradient(#f08fb0,#dd6a91 55%,#c9527c);display:flex;align-items:center;
  box-shadow:0 2px 4px rgba(0,0,0,.3)}
.main-nav a{flex:none;white-space:nowrap;color:var(--white);font-size:13px;padding:0 17px;height:100%;display:flex;align-items:center;
  border-right:1px solid rgba(255,255,255,.25)}
.main-nav a:last-child{border:none}
.main-nav .home{width:50px;justify-content:center;padding:0;background:rgba(0,0,0,.06)}
.featured{position:absolute;left:156px;top:159px;width:655px;height:294px;overflow:hidden;
  background:radial-gradient(ellipse at 50% 45%,#f3a6df 0%,#e79ac4 30%,#f2b9bf 55%,#6e8a4c 90%)}
.ribbon{position:absolute;left:-6px;top:-6px;width:80px;height:80px;overflow:hidden}
.ribbon span{position:absolute;left:-26px;top:20px;width:110px;height:20px;transform:rotate(-45deg);
  background:#b51f2b;color:var(--white);font-size:9px;font-weight:700;text-align:center;line-height:20px;letter-spacing:1px}
.side-list{position:absolute;left:815px;top:159px;width:231px;height:294px;background:var(--white)}
.side-item{height:74px;display:flex;gap:10px;padding:9px 10px;border-bottom:1px solid #f0cdd9;background:var(--pink-soft)}
.side-item:first-child{background:var(--white)}
.thumb{width:70px;height:52px;border:3px solid #f3dbe4;flex:none}
.side-item h3{font-size:11px;color:var(--rose-title);text-transform:uppercase;margin-bottom:3px}
.side-item p{font-size:11px;line-height:14px;color:#555;max-width:118px}
.products{position:absolute;left:156px;top:481px;width:890px;height:279px;background:var(--white);
  border-top:8px solid var(--pink-light);border-radius:4px 4px 0 0;display:flex;padding:14px 0 24px}
.product{position:relative;width:216.5px;padding:0 13px 0 26px;border-right:1px solid #e6e6e6}
.product:first-child{width:228px}
.product:last-child{border:none}
.product h2{font-size:14px;color:var(--rose-title)}
.product .price{font-size:12px;font-weight:700;margin-top:5px}
.product-photo{position:absolute;left:50px;top:62px;width:110px;height:120px;border-radius:45% 45% 20% 20%}
.cart-btn{position:absolute;left:26px;top:200px;width:89px;height:30px;border-radius:3px;
  background:linear-gradient(#4a4a4a,var(--button));color:var(--white);font-size:12px;display:flex;align-items:center;justify-content:center}
.more{position:absolute;left:154px;top:205px;font-size:11px;color:var(--pink);border-bottom:1px dotted var(--pink)}
.next{position:absolute;left:1022px;top:599px;width:23px;height:24px;background:#ddd;display:flex;align-items:center;justify-content:center}
.site-footer{position:absolute;left:0;top:823px;width:1200px;height:76px;background:var(--footer);
  border-top:3px solid #222;text-align:center;font-size:10px;color:#ddd;padding-top:30px;line-height:17px}
.to-top{position:absolute;left:1000px;top:802px;width:43px;height:43px;border-radius:50%;
  background:radial-gradient(#bdbdbd,#8a8a8a);color:var(--white);font-size:8px;font-weight:700;
  display:flex;flex-direction:column;align-items:center;justify-content:center}
</style>
</head>
<body>
<div class="flourish flourish-left" role="img" aria-label="Faint floral swirl decoration"></div>
<div class="flourish flourish-top" role="img" aria-label="Faint floral swirl decoration"></div>
<div class="flourish flourish-right" role="img" aria-label="Faint flower decoration"></div>
<header>
  <a class="brand" href="#"><span class="brand-dot"></span>Wrenfield Flowers</a>
  <div class="search-tab"></div>
  <div class="search"><span>Search...</span><i></i>
    <svg width="14" height="14" viewBox="0 0 14 14"><circle cx="5.5" cy="5.5" r="4" fill="none" stroke="#555" stroke-width="2"/><line x1="8.5" y1="8.5" x2="13" y2="13" stroke="#555" stroke-width="2.4"/></svg></div>
  <nav class="account-links">
    <a href="#"><span class="icon-round"><svg width="12" height="12" viewBox="0 0 12 12"><circle cx="4" cy="4" r="3" fill="#fff"/><line x1="5" y1="5" x2="11" y2="11" stroke="#fff" stroke-width="2"/></svg></span>My Account</a>
    <a href="#"><span class="icon-round"><svg width="13" height="12" viewBox="0 0 13 12"><path d="M0 1h2l2 7h7l2-5H3" fill="none" stroke="#fff" stroke-width="1.6"/><circle cx="5" cy="10.5" r="1.3" fill="#fff"/><circle cx="10" cy="10.5" r="1.3" fill="#fff"/></svg></span>My Cart ( 0 )</a>
  </nav>
  <nav class="main-nav">
    <a class="home" href="#"><svg width="16" height="14" viewBox="0 0 16 14"><path d="M8 0L0 7h2v7h4V9h4v5h4V7h2z" fill="#fff"/></svg></a>
    <a href="#">Buy Flowers</a><a href="#">Season's Collection</a><a href="#">Weddings &amp; Contracts</a>
    <a href="#">Gifts &amp; Accessories</a><a href="#">Updates</a><a href="#">Blog</a><a href="#">FAQ</a><a href="#">Contact</a>
  </nav>
</header>
<main>
  <section class="featured" role="img" aria-label="Pink roses arranged in a heart shape on a pink background">
    <div class="ribbon"><span>FEATURED</span></div>
  </section>
  <aside class="side-list">
    <div class="side-item"><div class="thumb" role="img" aria-label="Pink roses" style="background:#f0b3cf"></div><div><h3>Pink Roses</h3><p>Lorem Ipsum is simply dummy text of the printing.</p></div></div>
    <div class="side-item"><div class="thumb" role="img" aria-label="Yellow gerbera" style="background:#f2c65e"></div><div><h3>Sunny Yellow</h3><p>Lorem Ipsum is simply dummy text of the printing.</p></div></div>
    <div class="side-item"><div class="thumb" role="img" aria-label="Tulips" style="background:#e98aa8"></div><div><h3>All Tulips</h3><p>Lorem Ipsum is simply dummy text of the printing.</p></div></div>
    <div class="side-item"><div class="thumb" role="img" aria-label="Orange gerberas" style="background:#f0935a"></div><div><h3>Sunny Deals</h3><p>Lorem Ipsum is simply dummy text of the printing.</p></div></div>
  </aside>
  <section class="products">
    <article class="product"><h2>Amazonia</h2><p class="price">$39.99</p>
      <div class="product-photo" role="img" aria-label="Tropical bouquet in a glass vase" style="background:radial-gradient(#e8563a,#f2a07a 55%,#fff 72%)"></div>
      <a class="cart-btn" href="#">Add to cart</a><a class="more" href="#">View more...</a></article>
    <article class="product"><h2>Reflection</h2><p class="price">$13</p>
      <div class="product-photo" role="img" aria-label="Pink and white rose bouquet" style="background:radial-gradient(#e7a6b6,#f1d4da 55%,#fff 72%)"></div>
      <a class="cart-btn" href="#">Add to cart</a><a class="more" href="#">View more...</a></article>
    <article class="product"><h2>Peace</h2><p class="price">$30.99</p>
      <div class="product-photo" role="img" aria-label="White lily bouquet" style="background:radial-gradient(#e5e8d2,#eef0e4 55%,#fff 72%)"></div>
      <a class="cart-btn" href="#">Add to cart</a><a class="more" href="#">View more...</a></article>
    <article class="product"><h2>Twilight</h2><p class="price">Free!</p>
      <div class="product-photo" role="img" aria-label="Lilac and white bouquet in a vase" style="background:radial-gradient(#c9b0dc,#e4dbec 55%,#fff 72%)"></div>
      <a class="cart-btn" href="#">Add to cart</a><a class="more" href="#">View more...</a></article>
  </section>
  <a class="next" href="#"><svg width="8" height="12" viewBox="0 0 8 12"><path d="M1 1l5 5-5 5" fill="none" stroke="#fff" stroke-width="2.4"/></svg></a>
</main>
<footer class="site-footer">
  <p>Copyright © 2013, Wrenfield Flowers, All rights reserved.</p>
  <p>Developed by Northpixel Studio</p>
</footer>
<a class="to-top" href="#"><svg width="12" height="8" viewBox="0 0 12 8"><path d="M1 7l5-5 5 5" fill="none" stroke="#fff" stroke-width="2.4"/></svg>TOP</a>
</body>
</html>
```